Verdant Orchard - Stationery Design Project

We need a stationary for our business. We grow roots and fruits in Central and South America, we import and distribute in FL, USA. We do fresh and frozen products.

Target Market(s)

Small and big supermarkets, wholesalers, traders, distributors, etc

Industry/Entity Type

Business

```html
<!DOCTYPE html>
<html lang="en">
<head>
<meta charset="utf-8">
<title>Verdant Orchard – Stationery</title>
<link href="https://fonts.googleapis.com/css2?family=Montserrat:wght@400;600&display=swap" rel="stylesheet">
<style>
  :root {
    --backdrop: #8c8e80;
    --paper: #f4f4f4;
    --paper-shade: #e6e6e6;
    --teal: #1898b1;
    --teal-light: #3aaec3;
    --brand-orange: #e5861c;
    --olive: #4d5b2b;
    --ink-soft: #6a6a6a;
  }
  * { box-sizing: border-box; margin: 0; padding: 0; }
  html, body { width: 1200px; height: 1000px; overflow: hidden; }
  body {
    background: var(--backdrop);
    font-family: "Montserrat", Arial, sans-serif;
    position: relative;
  }
  .piece { position: absolute; background: var(--paper); overflow: hidden; }

  .brand-name {
    font-family: "Montserrat", Arial, sans-serif;
    font-weight: 600;
    color: var(--brand-orange);
    letter-spacing: 0.04em;
    text-transform: uppercase;
    display: flex;
    align-items: center;
    gap: 8px;
    white-space: nowrap;
  }
  .brand-name .brand-dot {
    width: 10px; height: 10px; border-radius: 50%;
    background: var(--olive); flex: none;
  }
  .brand-name.on-teal { color: #ffffff; }
  .brand-name.on-teal .brand-dot { background: #ffffff; }

  .leaf-decoration {
    position: absolute;
    background: radial-gradient(ellipse at 40% 60%, rgba(255,255,255,0.14), rgba(255,255,255,0) 70%);
  }
  .leaf-decoration.on-paper {
    background: radial-gradient(ellipse at 50% 60%, rgba(0,0,0,0.05), rgba(0,0,0,0) 70%);
  }

  /* Folder */
  .folder { left: 40px; top: 60px; width: 360px; height: 480px; }
  .folder-flap { height: 150px; display: flex; align-items: center; justify-content: center; background: var(--paper); }
  .folder-flap .brand-name { font-size: 22px; }
  .folder-body { position: absolute; left: 0; top: 150px; width: 100%; height: 330px; background: var(--teal); }
  .folder-body .leaf-decoration { left: 40px; bottom: 0; width: 300px; height: 200px; }

  /* Letterhead */
  .letterhead { left: 430px; top: 60px; width: 340px; height: 480px; }
  .letterhead-header { padding: 34px 0 10px; display: flex; justify-content: center; }
  .letterhead-header .brand-name { font-size: 16px; }
  .letterhead-rule { margin: 0 24px; height: 1px; background: #8b8fb8; }
  .letterhead .leaf-decoration { right: 10px; bottom: 50px; width: 200px; height: 140px; }
  .contact-band {
    position: absolute; left: 0; bottom: 0; width: 100%;
    background: var(--teal); color: #ffffff;
    display: flex; gap: 24px; padding: 8px 16px;
    font-size: 7px; line-height: 1.6;
  }
  .contact-band .contact-col + .contact-col { border-left: 1px solid rgba(255,255,255,0.5); padding-left: 14px; }
  .contact-line { display: flex; align-items: center; gap: 5px; }
  .contact-line svg { width: 7px; height: 7px; fill: currentColor; flex: none; }

  /* Envelope */
  .envelope { left: 800px; top: 60px; width: 360px; height: 180px; }
  .envelope-flap-strip { height: 14px; background: var(--teal); }
  .envelope-brand { position: absolute; left: 26px; top: 34px; }
  .envelope-brand .brand-name { font-size: 13px; }
  .envelope .leaf-decoration { right: 20px; bottom: 30px; width: 120px; height: 90px; }
  .envelope .contact-band { padding: 6px 14px; }

  /* Business cards */
  .card { width: 170px; height: 100px; top: 270px; }
  .card-front { left: 800px; background: var(--teal); display: flex; align-items: center; justify-content: center; }
  .card-front .brand-name { font-size: 11px; }
  .card-back { left: 990px; padding: 12px; }
  .card-back .brand-name { font-size: 9px; }
  .card-person { position: absolute; right: 12px; top: 44px; font-size: 8px; font-weight: 600; color: var(--ink-soft); letter-spacing: 0.06em; }
  .card-details { position: absolute; left: 12px; bottom: 12px; font-size: 6px; line-height: 1.7; color: var(--ink-soft); }
  .card-back .leaf-decoration { right: 0; bottom: 0; width: 80px; height: 60px; }

  /* Disc sleeve and disc */
  .disc-sleeve { left: 800px; top: 400px; width: 160px; height: 160px; background: #ffffff; display: flex; align-items: center; justify-content: center; }
  .disc-sleeve .brand-name { font-size: 11px; }
  .disc { position: absolute; left: 980px; top: 400px; width: 160px; height: 160px; }
</style>
</head>
<body>

  <section class="piece folder" aria-label="Presentation folder">
    <div class="folder-flap">
      <div class="brand-name"><span class="brand-dot"></span>Verdant Orchard</div>
    </div>
    <div class="folder-body">
      <div class="leaf-decoration" role="img" aria-label="Faint large leaf motif"></div>
    </div>
  </section>

  <section class="piece letterhead" aria-label="Letterhead">
    <div class="letterhead-header">
      <div class="brand-name"><span class="brand-dot"></span>Verdant Orchard</div>
    </div>
    <div class="letterhead-rule"></div>
    <div class="leaf-decoration on-paper" role="img" aria-label="Faint leaf motif"></div>
    <div class="contact-band">
      <div class="contact-col">
        <div class="contact-line"><svg viewBox="0 0 10 10"><path d="M2 1h2l1 2-1 1a5 5 0 0 0 2 2l1-1 2 1v2a1 1 0 0 1-1 1A8 8 0 0 1 1 2a1 1 0 0 1 1-1z"/></svg>305 555 0142</div>
        <div class="contact-line"><svg viewBox="0 0 10 10"><path d="M2 1h2l1 2-1 1a5 5 0 0 0 2 2l1-1 2 1v2a1 1 0 0 1-1 1A8 8 0 0 1 1 2a1 1 0 0 1 1-1z"/></svg>305 555 0187</div>
      </div>
      <div class="contact-col">
        <div class="contact-line"><svg viewBox="0 0 10 10"><path d="M0 5l10-4-3 8-2-3z"/></svg>www.verdantorchard.com</div>
        <div class="contact-line"><svg viewBox="0 0 10 10"><path d="M0 5l10-4-3 8-2-3z"/></svg>info@verdantorchard.com</div>
      </div>
    </div>
  </section>

  <section class="piece envelope" aria-label="Envelope">
    <div class="envelope-flap-strip"></div>
    <div class="envelope-brand">
      <div class="brand-name"><span class="brand-dot"></span>Verdant Orchard</div>
    </div>
    <div class="leaf-decoration on-paper" role="img" aria-label="Faint leaf motif"></div>
    <div class="contact-band">
      <div class="contact-col">
        <div class="contact-line"><svg viewBox="0 0 10 10"><path d="M2 1h2l1 2-1 1a5 5 0 0 0 2 2l1-1 2 1v2a1 1 0 0 1-1 1A8 8 0 0 1 1 2a1 1 0 0 1 1-1z"/></svg>305 555 0142</div>
        <div class="contact-line"><svg viewBox="0 0 10 10"><path d="M2 1h2l1 2-1 1a5 5 0 0 0 2 2l1-1 2 1v2a1 1 0 0 1-1 1A8 8 0 0 1 1 2a1 1 0 0 1 1-1z"/></svg>305 555 0187</div>
      </div>
      <div class="contact-col">
        <div class="contact-line"><svg viewBox="0 0 10 10"><path d="M0 5l10-4-3 8-2-3z"/></svg>www.verdantorchard.com</div>
        <div class="contact-line"><svg viewBox="0 0 10 10"><path d="M0 5l10-4-3 8-2-3z"/></svg>info@verdantorchard.com</div>
      </div>
    </div>
  </section>

  <section class="piece card card-front" aria-label="Business card front">
    <div class="brand-name on-teal"><span class="brand-dot"></span>Verdant Orchard</div>
  </section>

  <section class="piece card card-back" aria-label="Business card back">
    <div class="brand-name"><span class="brand-dot"></span>Verdant Orchard</div>
    <div class="card-person">MARCO RUIZ</div>
    <div class="card-details">
      <div>305 555 0142</div>
      <div>marco@verdantorchard.com</div>
      <div>verdantorchard.com</div>
    </div>
    <div class="leaf-decoration on-paper" role="img" aria-label="Faint leaf motif"></div>
  </section>

  <section class="piece disc-sleeve" aria-label="Disc sleeve">
    <div class="brand-name"><span class="brand-dot"></span>Verdant Orchard</div>
  </section>

  <svg class="disc" viewBox="0 0 160 160" aria-label="Disc label">
    <circle cx="80" cy="80" r="78" fill="#ffffff"/>
    <circle cx="80" cy="80" r="22" fill="#d8d8d8"/>
    <circle cx="80" cy="80" r="14" fill="#bdbdbd"/>
    <circle cx="80" cy="80" r="7" fill="var(--backdrop)"/>
    <text x="80" y="126" text-anchor="middle" font-family="Montserrat, Arial, sans-serif" font-weight="600" font-size="8" fill="#e5861c" letter-spacing="0.4">VERDANT ORCHARD</text>
  </svg>

</body>
</html>
```